Business Cards for Demolition & Salvage Company

We are Licensed Demolition Contractors and this business card design is for our Salvage Yard. We recycle over 95% of the building materials removed from each demolition site in which we take to our Salvage Yard for resale eg. bricks, windows, doors, kitchens, stoves, lights, fencing etc so pretty much everything.
Updates

I forgot to note that single sided business card only please.

Reason: I would like to ask if designers could please submit or re-submit their designs edited to a single sided card only. The card also does not need space for an employee name or position as our general business contact details will suffice for this project. Primary colour must be ROYAL BLUE with no exceptions please. Much appreciated and thank you to all whom have submitted designs to date and I look forward to receiving your edited designs..

Industry/Entity Type

Building

Contact Information for Business Card

Tavelund Demolition & Salvage (WA) Pty Ltd
2413 Coralbrook Parkway
UPPER SWAN WA 6069
P: (08) 9371 5068
F: (08) 9371 7725
E: salvage@tvwreck.com.au
W: tavelunddemolition.com.au

Requirements
Must have
• We have a logo that has been with our Company since 1974 so he must be included in the design - file attached. As for colours, we have always used royal blue and again this must be the primary colour used in the design. Please keep the design simple.
Nice to have
• Card can include opening hours as follows:
Opening Hours:
Monday to Friday 8am - 5.00pm
Saturday 8am - 3pm
Closed Sunday's and public holidays

```html
<!DOCTYPE html>
<html lang="en">
<head>
<meta charset="utf-8">
<title>Tavelund Demolition &amp; Salvage – Business Card</title>
<link rel="stylesheet" href="https://fonts.googleapis.com/css2?family=EB+Garamond:wght@600&family=Arimo:wght@400&display=swap">
<style>
  :root {
    --backdrop: #e9e6e1;
    --card: #ffffff;
    --royal-blue: #5f82c0;
    --royal-blue-deep: #3f63a8;
    --ink: #1b1b1b;
    --ink-soft: #3a4150;
    --icon: #ffffff;
  }
  * { margin: 0; padding: 0; box-sizing: border-box; }
  html, body {
    width: 1200px; height: 800px; overflow: hidden;
    background: var(--backdrop);
  }
  .business-card {
    position: absolute;
    left: 100px; top: 95px;
    width: 1000px; height: 610px;
    background: var(--card);
    box-shadow: 0 10px 30px rgba(0,0,0,0.18);
    overflow: hidden;
  }
  .contact-panel {
    position: absolute;
    left: 620px; top: 0;
    width: 380px; height: 460px;
    background: var(--royal-blue);
  }
  .brand {
    position: absolute;
    left: 60px; top: 150px;
    display: flex; align-items: center; gap: 22px;
  }
  .brand-mark {
    width: 96px; height: 96px; border-radius: 50%;
    background: var(--royal-blue-deep);
    flex: none;
  }
  .brand-name {
    font-family: "EB Garamond", Georgia, serif;
    font-weight: 600;
    font-size: 31px;
    line-height: 1.15;
    color: var(--ink);
  }
  .contact-list {
    position: absolute;
    left: 650px; top: 120px;
    list-style: none;
    font-family: "Arimo", Arial, sans-serif;
    font-size: 22px;
    color: var(--ink-soft);
  }
  .contact-item {
    display: flex; align-items: flex-start; gap: 18px;
    margin-bottom: 16px;
    line-height: 1.2;
  }
  .contact-icon {
    width: 24px; height: 24px; flex: none; margin-top: 1px;
  }
  .contact-icon * { fill: var(--icon); }
  .opening-hours {
    position: absolute;
    left: 110px; top: 490px;
    display: flex; gap: 16px; align-items: baseline;
  }
  .hours-label {
    font-family: "EB Garamond", Georgia, serif;
    font-weight: 600;
    font-size: 28px;
    color: var(--ink);
    white-space: nowrap;
  }
  .hours-text {
    font-family: "Arimo", Arial, sans-serif;
    font-size: 20px;
    line-height: 1.35;
    color: var(--ink-soft);
  }
</style>
</head>
<body>
  <main class="business-card">
    <div class="contact-panel"></div>

    <div class="brand">
      <div class="brand-mark"></div>
      <p class="brand-name">Tavelund Demolition<br>&amp; Salvage (WA) Pty Ltd</p>
    </div>

    <ul class="contact-list">
      <li class="contact-item">
        <svg class="contact-icon" viewBox="0 0 24 24"><path d="M12 1a8 8 0 0 0-8 8c0 6 8 14 8 14s8-8 8-14a8 8 0 0 0-8-8zm0 11a3 3 0 1 1 0-6 3 3 0 0 1 0 6z"/></svg>
        <span>2413 Coralbrook Parkway<br>UPPER SWAN WA 6069</span>
      </li>
      <li class="contact-item">
        <svg class="contact-icon" viewBox="0 0 24 24"><path d="M6.6 10.8a15 15 0 0 0 6.6 6.6l2.2-2.2a1 1 0 0 1 1-.25 11.4 11.4 0 0 0 3.6.57 1 1 0 0 1 1 1V20a1 1 0 0 1-1 1A17 17 0 0 1 3 4a1 1 0 0 1 1-1h3.5a1 1 0 0 1 1 1c0 1.25.2 2.45.57 3.6a1 1 0 0 1-.25 1z"/></svg>
        <span>(08) 9371 5068</span>
      </li>
      <li class="contact-item">
        <svg class="contact-icon" viewBox="0 0 24 24"><rect x="6" y="2" width="12" height="6"/><rect x="2" y="9" width="20" height="10" rx="2"/><rect x="6" y="16" width="12" height="6"/></svg>
        <span>(08) 9371 7725</span>
      </li>
      <li class="contact-item">
        <svg class="contact-icon" viewBox="0 0 24 24"><path d="M2 5h20v14H2z M3 6l9 7 9-7" fill-rule="evenodd"/><path d="M2 5h20L12 12.5z" fill-opacity="0.6"/></svg>
        <span>salvage@tvwreck.com.au</span>
      </li>
      <li class="contact-item">
        <svg class="contact-icon" viewBox="0 0 24 24"><path d="M12 2a10 10 0 1 0 0 20 10 10 0 0 0 0-20zm6.9 6h-3a15 15 0 0 0-1.3-4 8 8 0 0 1 4.3 4zM12 4c.8 1.1 1.5 2.5 1.9 4h-3.8c.4-1.5 1.1-2.9 1.9-4zM4.3 14a8 8 0 0 1 0-4h3.4a16 16 0 0 0 0 4zm.8 2h3a15 15 0 0 0 1.3 4 8 8 0 0 1-4.3-4zm3-8h-3a8 8 0 0 1 4.3-4 15 15 0 0 0-1.3 4zM12 20c-.8-1.1-1.5-2.5-1.9-4h3.8c-.4 1.5-1.1 2.9-1.9 4zm2.3-6H9.7a14 14 0 0 1 0-4h4.6a14 14 0 0 1 0 4zm.3 6a15 15 0 0 0 1.3-4h3a8 8 0 0 1-4.3 4zm1.7-6a16 16 0 0 0 0-4h3.4a8 8 0 0 1 0 4z"/></svg>
        <span>tavelunddemolition.com.au</span>
      </li>
    </ul>

    <div class="opening-hours">
      <span class="hours-label">Opening Hours:</span>
      <p class="hours-text">Monday to Friday 8am - 5.00pm &nbsp;Saturday 8am - 3pm<br>Closed Sunday's and public holidays</p>
    </div>
  </main>
</body>
</html>
```